ROSE WINE LABEL

WE NEED A LABEL DESIGN FOR A NEW ROSE WINE MADE IN MEXICO. THIS IS A NEW WINARY THAT WANTS TO DO SOMETHING DIFFERENT FOR THE WINE INDUSTRY IN MEXICO, EXCELENT QUALITY OF WINE ACCESIBLE FOR EVERYONE. WINE CULTURE IN MEXICO IS NOT GOOD, WE WANT TO INNOVATE IN THE MARKET, BRING WINE TO YOUNG PEOPLE WITHOUT MAKING IT SEAM LIKE A "LUXURY" PRODUCT, LET THEM KNOW THAT YOU CAN DRINK WINE EVERYDAY EVERYTIME, SOMETHING EASY TO ANALYZE, DRINK AND UNDERSTAND, SOMETHING TO LET KNOW THE CONSUMERS ABOUT THE GOOD QUALITY OF WINE YOU CAN FIND IN MEXICO. I WANT TO SEE A DIFFERENT DESIGN. WE WANT TO KEEP WORKING WITH THE DESIGNER FOR THE REST OF THE LABELS, AROUND 6-7. THE NAME OF THE WINARY IS "VINOS DEL ROBLEDAL" AND THE NAMES OF THE WINES ARE GOING TO HAVE THE "ROBLEDAL" AND THE DIFFERENT FINE ARTS LIKE PAINTING, DANCE, LITERATURE, ETC.
THE BOTTLE OF THIS WINE IS GOING TO BE REGULAR SHAPE ALSO KNOWN AS BODEAUX, TRANSPARENT AND LIGHT GREEN ALSO KNOWN AS "GREEN CHAMPAGNE", SILVER & BLACK CAPSULE.

Requirements
Must have
• THE LABEL MUST HAVE THE NAME OF THE WINE "BAILE DE LA ROBLEDANA" AND IN A SMALLER FONT "QUERÉTARO, MÉXICO"
Nice to have
• A COLORFUL AND MODERN DESIGN, I AM ATTACHING THE LOGO OF THE WINARY. IT IS NOT NECESARY TO ADD IT TO THE LABEL, BUT PERHAPS SOMEONE IS INTERESTED IN THE "VR" OF THE DESIGN FROM INSIDE THE SHELL.
Should not have
• THE DESIGN SHOULD BE ABLE TO FIT IN A REGULAR FORM, RECTANGULAR, SQUARE, OR CIRCLE, NO SPECIAL DIE CUTTING CAN BE MADE TO THE LABEL.

```html
<!DOCTYPE html>
<html lang="es">
<head>
<meta charset="utf-8">
<title>Vinos del Robledal — Baile de la Robledana</title>
<link rel="stylesheet" href="https://fonts.googleapis.com/css2?family=Cinzel:wght@400&family=Libre+Baskerville:wght@700&family=Oswald:wght@300&display=swap">
<style>
  :root {
    --page: #f3ece0;
    --label: #3a0f2a;
    --label-edge: #2a0a1e;
    --glow-rose: #b8325e;
    --glow-coral: #e0607a;
    --frame: #ff5a6e;
    --crest: #ff4f66;
    --accent: #ffb3c1;
    --ink: #fff5f7;
    --ink-soft: #f6dde3;
  }
  * { margin: 0; padding: 0; box-sizing: border-box; }
  html, body { width: 1200px; height: 1000px; overflow: hidden; }
  body { background: var(--page); position: relative; }

  .label {
    position: absolute;
    left: 372px;
    top: 60px;
    width: 457px;
    height: 880px;
    background: linear-gradient(170deg, var(--label) 0%, var(--label-edge) 100%);
    color: var(--ink);
    overflow: hidden;
  }
  .label__frame {
    position: absolute;
    inset: 11px;
    border: 1.5px solid var(--frame);
  }
  .label__decoration {
    position: absolute;
    left: 40px;
    top: 150px;
    width: 377px;
    height: 560px;
    border-radius: 45% 45% 40% 40%;
    background: radial-gradient(ellipse at 50% 42%, rgba(224,96,122,0.55) 0%, rgba(184,50,94,0.35) 45%, rgba(58,15,42,0) 78%);
  }

  .brand-mark {
    position: absolute;
    top: 62px;
    left: 0;
    right: 0;
    display: flex;
    justify-content: center;
    align-items: center;
    gap: 10px;
  }
  .brand-mark__square { width: 14px; height: 14px; background: var(--crest); }
  .brand-mark__name {
    font-family: "Cinzel", serif;
    font-size: 56px;
    color: var(--crest);
    letter-spacing: 2px;
    line-height: 1;
  }

  .title-block {
    position: absolute;
    width: 500px;
    height: 110px;
    left: calc(256px - 250px);
    top: calc(443px - 55px);
    transform: rotate(-90deg);
  }
  .winery-name {
    font-family: "Cinzel", serif;
    font-weight: 400;
    font-size: 44px;
    line-height: 56px;
    text-align: center;
    white-space: nowrap;
    letter-spacing: 1px;
  }
  .title-rule { display: block; width: 440px; height: 8px; margin: 4px auto 6px; }
  .origin {
    font-family: "Cinzel", serif;
    font-size: 21px;
    letter-spacing: 1px;
    text-align: right;
    padding-right: 60px;
    color: var(--accent);
  }

  .wine-name {
    position: absolute;
    top: 714px;
    left: 30px;
    right: 30px;
    font-family: "Cinzel", serif;
    font-weight: 400;
    font-size: 20px;
    letter-spacing: 2px;
    text-align: center;
    color: var(--crest);
  }
  .description {
    position: absolute;
    top: 748px;
    left: 70px;
    right: 70px;
    font-family: "Libre Baskerville", serif;
    font-weight: 700;
    font-size: 11px;
    line-height: 15px;
    text-align: center;
    color: var(--ink-soft);
  }
  .spec {
    position: absolute;
    top: 822px;
    font-family: "Oswald", sans-serif;
    font-weight: 300;
    font-size: 37px;
    line-height: 1;
    color: var(--ink);
  }
  .spec small { font-size: 15px; margin-left: 3px; color: var(--accent); }
  .spec--abv { left: 38px; }
  .spec--volume { right: 40px; }
</style>
</head>
<body>
  <section class="label">
    <div class="label__decoration" role="img" aria-label="Faint large monogram decoration behind the label text"></div>
    <div class="label__frame"></div>

    <div class="brand-mark">
      <span class="brand-mark__square"></span>
      <span class="brand-mark__name">VR</span>
    </div>

    <div class="title-block">
      <p class="winery-name">Vinos del Robledal</p>
      <svg class="title-rule" viewBox="0 0 440 8" aria-hidden="true">
        <line x1="4" y1="4" x2="436" y2="4" stroke="#ffb3c1" stroke-width="1"/>
        <circle cx="4" cy="4" r="3" fill="#ffb3c1"/>
        <circle cx="436" cy="4" r="3" fill="#ffb3c1"/>
      </svg>
      <p class="origin">Querétaro, México</p>
    </div>

    <h1 class="wine-name">Baile de la Robledana</h1>
    <p class="description">Fresh rosé from the highlands of Querétaro, crafted to be shared on any day. Bright red fruit, a clean finish and a light touch that invites another glass with friends. Serve chilled and enjoy.</p>

    <p class="spec spec--abv">11%<small>VOL.</small></p>
    <p class="spec spec--volume">750<small>ML</small></p>
  </section>
</body>
</html>
```